Food delivery wordpress design

need food delivery wordpress design for my site, here's the requirements
1. site must be pixel perfect , clean and professional
2. logo provided and must be match with the color scheme
3. pages : home , about us , faq , vendor registration

*** this is a information site no order can be made from the site, the site will show how things work , how to register as vendor , how to use the app , you may use any stock photo from lumbrevault and send me the code, i will purchase it

you may use any of the logo to play with it

***** It must look scale and not looks like template where I can purchase elsewhere
Updates

the designer told me he can't work as he got his personal problem, please check his message

Target Market(s)

those who prefer to purchase online

Font styles to use
Sans Serif

Requirements
Must have
• refer to zolvique.com/my
Nice to have
• everything user and vendor like to know

```html
<!DOCTYPE html>
<html lang="en">
<head>
<meta charset="utf-8">
<title>Dapurloka — Food Delivery</title>
<link href="https://fonts.googleapis.com/css2?family=Montserrat:wght@500;600;700;800&family=Roboto:wght@400;500;700&display=swap" rel="stylesheet">
<style>
:root{
  --orange:#f7a021;
  --orange-deep:#f39200;
  --orange-soft:#fde3b8;
  --ink:#2b2b2b;
  --text:#4a4a4a;
  --muted:#6b6b6b;
  --bg-light:#f5f5f5;
  --bg-gray:#f1f1f1;
  --white:#ffffff;
}
*{box-sizing:border-box;margin:0;padding:0}
html,body{width:1200px;height:4471px;overflow:hidden}
body{position:relative;background:var(--white);font-family:Roboto,Arial,sans-serif;color:var(--text)}
.abs{position:absolute}
h1,h2,h3,h4{font-family:Montserrat,Arial,sans-serif;color:var(--ink)}
.mark{position:absolute;display:flex;gap:8px;align-items:center}
.mark i{display:block;width:14px;height:12px;border-radius:6px;background:var(--ink)}
.mark b{display:block;width:58px;height:10px;border-radius:5px;background:var(--ink)}
.mark.light i,.mark.light b{background:var(--white)}

/* hero */
.hero{position:absolute;left:0;top:0;width:1200px;height:640px;background:var(--bg-light);overflow:hidden}
.brand{position:absolute;left:100px;top:32px;display:flex;align-items:center;gap:10px}
.brand-dot{width:50px;height:50px;border-radius:50%;background:var(--orange)}
.brand-name{font-family:Montserrat,sans-serif;font-weight:700;font-size:34px;color:var(--ink);letter-spacing:-0.5px}
.nav{position:absolute;left:592px;top:51px;display:flex;gap:29px;font-family:Montserrat,sans-serif;font-size:16px;color:var(--white)}
.nav a{color:var(--white);text-decoration:none;font-weight:500}
.nav a.active{font-weight:700}
.hero-title{position:absolute;left:107px;top:222px;font-size:50px;line-height:58px;font-weight:800;color:var(--ink)}
.btn{position:absolute;display:flex;align-items:center;justify-content:center;font-family:Montserrat,sans-serif;font-weight:600;font-size:13px;letter-spacing:.3px;text-transform:uppercase}
.btn-fill{background:var(--orange);color:var(--white)}
.btn-line{border:2px solid var(--ink);color:var(--ink);background:transparent}
.dots{position:absolute;left:105px;top:574px;display:flex;gap:6px}
.dots span{width:14px;height:14px;border:2px solid var(--ink);border-radius:50%}
.dots span.on{width:18px;height:18px;margin-top:-2px}

/* how things work */
.steps{position:absolute;left:0;top:640px;width:1200px;height:755px;background:var(--bg-light)}
.sec-title{position:absolute;left:0;width:1200px;text-align:center;font-weight:700;font-size:38px}
.step{position:absolute;width:270px;text-align:center}
.step h3{font-size:18px;font-weight:600;margin-bottom:18px}
.step p{font-size:14px;line-height:21px;color:var(--muted)}

/* vendor */
.vendor-title{position:absolute;left:737px;top:1525px;font-size:40px;line-height:50px;font-weight:800}
.vendor-text{position:absolute;left:737px;top:1683px;width:360px;font-size:14.5px;line-height:22px;color:var(--muted)}

/* app */
.app{position:absolute;left:0;top:2030px;width:1200px;height:900px;background:var(--bg-gray)}
.feat{position:absolute;width:300px}
.feat h4{font-size:18px;font-weight:600;margin-bottom:8px}
.feat p{font-size:13.5px;line-height:19px;color:var(--muted)}
.feat.left{text-align:right}
.feat-icon{position:absolute;width:78px;height:78px;border-radius:50%;background:var(--orange)}
.feat-icon::after{content:"";position:absolute;left:22px;top:22px;width:34px;height:34px;border:3px solid var(--white);border-radius:6px}
.phone{position:absolute;left:478px;top:2301px;width:243px;height:499px;border:9px solid #1d1d1d;border-radius:34px;background:var(--white)}
.phone-mascot{position:absolute;left:42px;top:75px;width:140px;height:120px;border-radius:50%;background:radial-gradient(circle,var(--orange) 55%,var(--orange-soft))}
.phone-name{position:absolute;left:0;top:210px;width:225px;text-align:center;font-family:Montserrat,sans-serif;font-weight:700;font-size:34px;line-height:34px;color:var(--ink)}
.store{position:absolute;left:36px;width:155px;height:44px;border-radius:7px;background:#111}

/* services */
.services{position:absolute;left:0;top:2918px;width:1200px;height:1000px;background:linear-gradient(180deg,#f7a72e 0%,#f6a024 60%,#f19a1e 100%)}
.svc-title{position:absolute;left:0;top:3020px;width:1200px;text-align:center;font-family:Montserrat,sans-serif;font-weight:600;font-size:38px;line-height:50px;color:var(--white)}
.card{position:absolute;width:216px;height:292px;background:var(--white);text-align:center;box-shadow:0 4px 14px rgba(0,0,0,.08)}
.card .icon{width:100px;height:96px;margin:28px auto 0;border-radius:12px;background:linear-gradient(180deg,var(--orange-soft),#fbd08b)}
.card h4{font-size:16px;font-weight:700;margin:18px 0 14px}
.card p{font-size:13px;line-height:18px;color:var(--muted);padding:0 26px}

/* footer */
.footer{position:absolute;left:0;top:3917px;width:1200px;height:430px;background:var(--bg-light)}
.f-title{position:absolute;font-family:Montserrat,sans-serif;font-weight:700;font-size:17px;color:var(--ink)}
.f-text{position:absolute;font-size:13.5px;line-height:21px;color:var(--text)}
.input{position:absolute;left:344px;width:273px;height:38px;border:1px solid #cfcfcf;border-radius:19px;background:var(--white);font-size:12.5px;color:var(--text);padding:11px 14px}
.social{position:absolute;width:32px;height:32px;border:2px solid #3c5a99;border-radius:50%}
.contact{position:absolute;left:665px;width:230px}
.contact .ico{position:absolute;left:0;top:2px;width:18px;height:18px}
.contact .body{margin-left:36px;font-size:13.5px;line-height:20px;color:var(--ink)}
.links{position:absolute;left:928px;top:4050px;list-style:none;font-size:13.5px;line-height:27px;color:var(--ink)}
.copy{position:absolute;left:0;top:4397px;width:1200px;text-align:center;font-size:14px;color:var(--ink)}
</style>
</head>
<body>

<!-- HERO -->
<section class="hero">
  <svg class="abs" style="left:0;top:0" width="1200" height="640" aria-hidden="true">
    <path d="M470 0 H1200 V330 C1120 350 1060 300 990 330 C930 355 880 330 860 290 C820 220 760 230 690 210 C610 185 560 150 520 100 C495 70 480 35 470 0 Z" fill="var(--orange)"/>
  </svg>
  <div class="abs" role="img" aria-label="Mascot illustration of a running chef character with motion lines" style="left:570px;top:120px;width:520px;height:500px;border-radius:46% 52% 48% 50%;background:radial-gradient(circle at 55% 50%,var(--orange) 0 45%,#f5b85a 70%,rgba(245,245,245,0) 71%)"></div>
  <div class="brand"><span class="brand-dot"></span><span class="brand-name">dapurloka</span></div>
  <nav class="nav"><a class="active">Home</a><a>About us</a><a>Faq</a><a>Vendor Registration</a><a>Contact us</a></nav>
  <h1 class="hero-title">Despite these<br>uncertaintimes,<br>we're still here<br>to serve you</h1>
  <div class="btn btn-fill" style="left:106px;top:492px;width:164px;height:48px">Learn more</div>
  <div class="btn btn-line" style="left:284px;top:492px;width:162px;height:48px">Get started</div>
  <div class="dots"><span></span><span></span><span class="on"></span><span></span><span></span></div>
</section>

<!-- HOW THINGS WORK -->
<section class="steps">
  <h2 class="sec-title" style="top:65px">How Things Work</h2>
  <div class="mark" style="left:555px;top:138px"><i></i><b style="width:68px"></b></div>
  <svg class="abs" style="left:0;top:170px" width="1200" height="320" aria-hidden="true">
    <g fill="none" stroke="var(--ink)" stroke-width="3" stroke-dasharray="2 6" stroke-linecap="round">
      <path d="M132 255 C150 130 230 70 300 75 C370 80 430 150 444 234"/>
      <path d="M444 234 C450 330 560 380 620 365 C700 345 765 300 775 220"/>
      <path d="M775 220 C800 110 880 60 950 75 C1030 90 1065 170 1070 250"/>
    </g>
    <g fill="var(--white)" stroke="var(--orange)" stroke-width="4">
      <circle cx="132" cy="255" r="8"/><circle cx="444" cy="234" r="8"/><circle cx="775" cy="220" r="8"/><circle cx="1070" cy="250" r="8"/>
    </g>
    <g>
      <circle cx="269" cy="154" r="122" fill="var(--orange)"/>
      <circle cx="601" cy="154" r="122" fill="var(--orange)"/>
      <circle cx="934" cy="154" r="122" fill="var(--orange)"/>
      <circle cx="269" cy="144" r="108" fill="var(--white)"/>
      <circle cx="601" cy="144" r="108" fill="var(--white)"/>
      <circle cx="934" cy="144" r="108" fill="var(--white)"/>
      <circle cx="269" cy="280" r="18" fill="var(--orange)" stroke="var(--white)" stroke-width="3"/>
      <circle cx="601" cy="280" r="18" fill="var(--orange)" stroke="var(--white)" stroke-width="3"/>
      <circle cx="934" cy="280" r="18" fill="var(--orange)" stroke="var(--white)" stroke-width="3"/>
    </g>
    <g font-family="Montserrat,sans-serif" font-weight="700" font-size="17" fill="var(--white)" text-anchor="middle">
      <text x="269" y="286">1</text><text x="601" y="286">2</text><text x="934" y="286">3</text>
    </g>
  </svg>
  <div class="abs" role="img" aria-label="Icon of a support agent with headset" style="left:219px;top:264px;width:100px;height:100px;border-radius:18px;background:#ececec"></div>
  <div class="abs" role="img" aria-label="Icon of a checklist form being approved" style="left:551px;top:264px;width:100px;height:100px;border-radius:18px;background:#ececec"></div>
  <div class="abs" role="img" aria-label="Icon of the running chef mascot" style="left:884px;top:264px;width:100px;height:100px;border-radius:18px;background:#ececec"></div>
  <div class="step" style="left:134px;top:501px"><h3>Nemo enim voluptatem</h3><p>Sed ut perspiciatis unde omnis iste natus oluptatem accusantium doloremque laudantium, totam rem aperiam, eaque ipsa quae ab illo inventore veritatis et quasi architecto beatae vitae dicta sunt explicabo</p></div>
  <div class="step" style="left:466px;top:522px"><h3>Nemo enim voluptatem</h3><p>Sed ut perspiciatis unde omnis iste natus oluptatem accusantium doloremque laudantium, totam rem aperiam, eaque ipsa quae ab illo inventore veritatis et quasi architecto</p></div>
  <div class="step" style="left:799px;top:501px"><h3>Nemo enim voluptatem</h3><p>Sed ut perspiciatis unde omnis iste natus oluptatem accusantium doloremque laudantium, totam rem aperiam, eaque ipsa quae ab illo inventore veritatis et quasi architecto beatae vitae dicta sunt explicabo</p></div>
</section>

<!-- HOW TO REGISTER AS A VENDOR -->
<section>
  <div class="abs" role="img" aria-label="Illustration of a shop counter with a cashier serving a customer carrying shopping bags" style="left:104px;top:1511px;width:573px;height:382px;border-radius:48% 44% 40% 50%;background:radial-gradient(ellipse at 50% 55%,#e3ebfb 0 55%,#eef3fd 75%,rgba(255,255,255,0) 76%)"></div>
  <h2 class="vendor-title">How To Register<br>As A Vendor</h2>
  <div class="mark" style="left:737px;top:1648px"><i></i><b style="width:62px"></b></div>
  <p class="vendor-text">Sed ut perspiciatis unde omnis iste natus error sit voluptatem accusantium doloremque laudantium, totam rem aperiam, eaque ipsa quae ab illo inventore veritatis et quasi architecto beatae vitae dicta sunt explicabo.</p>
  <div class="btn btn-fill" style="left:737px;top:1826px;width:235px;height:46px">Vendor registration</div>
</section>

<!-- HOW TO USE THE APP -->
<section class="app">
  <svg class="abs" style="left:0;top:-60px" width="1200" height="130" aria-hidden="true">
    <path d="M0 0 H1200 V60 C1000 60 760 80 600 100 C400 125 180 115 0 70 Z" fill="var(--white)"/>
    <path d="M0 70 C180 115 400 125 600 100" fill="none" stroke="var(--ink)" stroke-width="12"/>
    <path d="M440 115 C520 108 560 104 600 100 C760 80 1000 60 1200 62" fill="none" stroke="var(--orange)" stroke-width="12"/>
  </svg>
</section>
<h2 class="sec-title" style="top:2163px">How To Use The App</h2>
<div class="mark" style="left:558px;top:2226px"><i></i><b style="width:62px"></b></div>

<svg class="abs" style="left:0;top:2360px" width="1200" height="320" aria-hidden="true">
  <g stroke="var(--ink)" stroke-width="2" stroke-dasharray="4 5">
    <line x1="412" y1="40" x2="412" y2="280"/><line x1="792" y1="40" x2="792" y2="280"/>
  </g>
</svg>
<div class="feat-icon" style="left:373px;top:2363px"></div>
<div class="feat-icon" style="left:373px;top:2500px"></div>
<div class="feat-icon" style="left:373px;top:2637px"></div>
<div class="feat-icon" style="left:753px;top:2363px"></div>
<div class="feat-icon" style="left:753px;top:2500px"></div>
<div class="feat-icon" style="left:753px;top:2637px"></div>

<div class="feat left" style="left:44px;top:2357px"><h4>Nemo enim ipsam</h4><p>Sed ut perspiciatis unde omnis iste natus error sit voluptatem accusantium doque laudantium, totam rem aperiam</p></div>
<div class="feat left" style="left:44px;top:2494px"><h4>Nemo enim ipsam</h4><p>Sed ut perspiciatis unde omnis iste natus error sit voluptatem accusantium doque laudantium, totam rem aperiam</p></div>
<div class="feat left" style="left:44px;top:2631px"><h4>Nemo enim ipsam</h4><p>Sed ut perspiciatis unde omnis iste natus error sit voluptatem accusantium doque laudantium, totam rem aperiam</p></div>
<div class="feat" style="left:856px;top:2357px"><h4>Nemo enim ipsam</h4><p>Sed ut perspiciatis unde omnis iste natus error sit voluptatem accusantium doque laudantium, totam rem aperiam</p></div>
<div class="feat" style="left:856px;top:2494px"><h4>Nemo enim ipsam</h4><p>Sed ut perspiciatis unde omnis iste natus error sit voluptatem accusantium doque laudantium, totam rem aperiam</p></div>
<div class="feat" style="left:856px;top:2631px"><h4>Nemo enim ipsam</h4><p>Sed ut perspiciatis unde omnis iste natus error sit voluptatem accusantium doque laudantium, totam rem aperiam</p></div>

<div class="phone">
  <div class="abs" style="left:72px;top:0;width:82px;height:16px;border-radius:0 0 10px 10px;background:#1d1d1d"></div>
  <div class="phone-mascot" role="img" aria-label="Running chef mascot illustration"></div>
  <div class="phone-name">dapur<br>loka</div>
  <div class="store" style="top:323px" role="img" aria-label="App store download badge"></div>
  <div class="store" style="top:378px" role="img" aria-label="Play store download badge"></div>
</div>

<!-- SERVICES -->
<section class="services" role="img" aria-label="Orange-toned photo of people enjoying a meal together"></section>
<svg class="abs" style="left:0;top:2870px" width="1200" height="110" aria-hidden="true">
  <path d="M0 0 H1200 V30 C1000 60 760 60 560 70 C360 80 180 60 0 40 Z" fill="var(--bg-gray)"/>
  <path d="M0 40 C180 60 360 80 560 70" fill="none" stroke="var(--ink)" stroke-width="12"/>
  <path d="M400 76 C460 74 510 72 560 70 C760 60 1000 60 1200 30" fill="none" stroke="var(--white)" stroke-width="10"/>
</svg>
<h2 class="svc-title">Learn more about the many different ways<br>we serve your everyday needs</h2>
<div class="mark light" style="left:558px;top:3142px"><i></i><b style="width:62px"></b></div>

<div class="card" style="left:132px;top:3210px"><div class="icon" role="img" aria-label="Food icon"></div><h4>Food</h4><p>Sed ut perspiciatis unde omnis iste natus error sit voluptatem accusantium doloremque laudantium, totam rem aperiam</p></div>
<div class="card" style="left:372px;top:3210px"><div class="icon" role="img" aria-label="Transport icon"></div><h4>Transport</h4><p>Sed ut perspiciatis unde omnis iste natus error sit voluptatem accusantium doloremque laudantium, totam rem aperiam</p></div>
<div class="card" style="left:612px;top:3210px"><div class="icon" role="img" aria-label="Delivery icon"></div><h4>Delivery</h4><p>Sed ut perspiciatis unde omnis iste natus error sit voluptatem accusantium doloremque laudantium, totam rem aperiam</p></div>
<div class="card" style="left:852px;top:3210px"><div class="icon" role="img" aria-label="Pay icon"></div><h4>Pay</h4><p>Sed ut perspiciatis unde omnis iste natus error sit voluptatem accusantium doloremque laudantium, totam rem aperiam</p></div>
<div class="card" style="left:132px;top:3530px"><div class="icon" role="img" aria-label="Rewards icon"></div><h4>Rewards</h4><p>Sed ut perspiciatis unde omnis iste natus error sit voluptatem accusantium doloremque laudantium, totam rem aperiam</p></div>
<div class="card" style="left:372px;top:3530px"><div class="icon" role="img" aria-label="Gifts icon"></div><h4>Gifts</h4><p>Sed ut perspiciatis unde omnis iste natus error sit voluptatem accusantium doloremque laudantium, totam rem aperiam</p></div>
<div class="card" style="left:612px;top:3530px"><div class="icon" role="img" aria-label="Insurance icon"></div><h4>Insurance</h4><p>Sed ut perspiciatis unde omnis iste natus error sit voluptatem accusantium doloremque laudantium, totam rem aperiam</p></div>
<div class="card" style="left:852px;top:3530px"><div class="icon" role="img" aria-label="Hotels icon"></div><h4>Hotels</h4><p>Sed ut perspiciatis unde omnis iste natus error sit voluptatem accusantium doloremque laudantium, totam rem aperiam</p></div>

<!-- FOOTER -->
<footer class="footer">
  <div class="abs" role="img" aria-label="Running chef mascot illustration" style="left:170px;top:80px;width:110px;height:100px;border-radius:50%;background:radial-gradient(circle,var(--orange) 55%,var(--orange-soft))"></div>
  <div class="abs" style="left:140px;top:190px;width:150px;text-align:center;font-family:Montserrat,sans-serif;font-weight:700;font-size:32px;line-height:32px;color:var(--ink)">dapur<br>loka</div>
  <span class="social" style="left:145px;top:300px"></span>
  <span class="social" style="left:184px;top:300px;border-color:#1da1f2"></span>
  <span class="social" style="left:222px;top:300px;border-color:#3f729b"></span>
  <span class="social" style="left:258px;top:300px;border-color:#e02a20"></span>

  <h4 class="f-title" style="left:344px;top:88px">SIGN UP FOR NEWSLETTER</h4>
  <p class="f-text" style="left:344px;top:137px;width:280px">excepteur sint occaecat cupidatat non proident, sunt in culpa qui officia deserunt</p>
  <div class="input" style="top:194px">Enter Name</div>
  <div class="input" style="top:244px">Enter email</div>
  <div class="btn btn-fill" style="left:344px;top:299px;width:138px;height:34px;border-radius:17px;font-size:13px">Subscribe</div>

  <h4 class="f-title" style="left:665px;top:90px">CONTACT US</h4>
  <div class="contact" style="top:140px">
    <svg class="ico" viewBox="0 0 20 20"><path d="M10 1a6 6 0 0 0-6 6c0 5 6 12 6 12s6-7 6-12a6 6 0 0 0-6-6zm0 8.5a2.5 2.5 0 1 1 0-5 2.5 2.5 0 0 1 0 5z" fill="var(--orange)"/></svg>
    <div class="body">Dapurloka<br>52 Lorong Kenanga<br>Taman Seri Indah</div>
  </div>
  <div class="contact" style="top:222px">
    <svg class="ico" viewBox="0 0 20 20"><path d="M4 2l3 0 2 5-2 1.5c1 2 2.5 3.5 4.5 4.5L13 11l5 2v3c0 1-1 2-2 2C8 18 2 12 2 4c0-1 1-2 2-2z" fill="var(--orange)"/></svg>
    <div class="body">Phone:<br>604 7719 2580</div>
  </div>
  <div class="contact" style="top:279px">
    <svg class="ico" viewBox="0 0 20 20"><rect x="1" y="4" width="18" height="12" rx="1.5" fill="var(--orange)"/><path d="M2 5l8 6 8-6" fill="none" stroke="var(--white)" stroke-width="1.5"/></svg>
    <div class="body">Email:<br>info@dapurloka.com</div>
  </div>
  <div class="contact" style="top:332px">
    <svg class="ico" viewBox="0 0 20 20"><rect x="5" y="2" width="10" height="6" fill="var(--orange)"/><rect x="2" y="8" width="16" height="10" rx="1.5" fill="var(--orange)"/><rect x="5" y="11" width="10" height="2" fill="var(--white)"/></svg>
    <div class="body">Fax:<br>604 7719 2599</div>
  </div>

  <h4 class="f-title" style="left:926px;top:90px">QUICK LINKS</h4>
</footer>
<ul class="links" style="top:4047px"><li>Home</li><li>About us</li><li>Faq</li><li>Vendor Registration</li><li>Contact us</li></ul>
<p class="copy">Dapurloka © 2020 All Rights Reserved | Privacy Policy</p>

</body>
</html>
```